Flyer-Design für Immobilienpräsentation
Zielgruppe
Meine Firma heißt 'Die Raumglanz Idee' und ich bin Home Stagerin und Einrichtungsberaterin. Ich bereite Immobilien für den Verkauf vor (Immobilienpräsentation), dass heißt ich 'richte' die jeweilige Immobilie mit Möbeln so ein, dass der Interessent ein 'hier-will-ich-wohnen Gefühl' beim betreten der Räumlichkeiten bekommt. Er soll sich in die jeweilige Immobilie im besten Fall sofort verlieben. Eingerichtete Immobilien verkaufen sich schneller da der Kunde ein Gefühl bekommt wie die Proportionen in den jeweiligen Räumen sind und keine kahle und nichts Aussagende Immobilie sieht. Die Zielgruppe sind in erster Linie Makler, Investoren, Bauträger aber auch private Personen.
Aufgabenstellung
Als einfachste Vorgabe dient meine Homepage und ein DIN Format ja meine Visitenkarte ist Waagerecht und da ich viele große Bilder gerne hätte bietet sich DIN A5 oder A6 an finde ich. Entweder Zweibruch Fensterfalz (siehe Druckpilot) oder wenn du eine Idee hast wie man es noch besser darstellen kann oder was besse aussieht bin ich offen.
In diesem Stil sollte es sein, bzw gerne auch etwas hochwertiger. Es sollen viele Fotos von einer gestageden Immobilie zu sehen sein inklusive eines Vorher-Nachher Bildes. Zu diesem Vorher- Nachher Bild gerne: mit Home Staging 11 Kaufzusagen innerhalb 2 Tage, verkauft zum Wunschpreis; ohne Home Staging 3 Monate auf den Markt, 15 Besichtigungen und keine Kaufzusage.
Text würde ich mich mehr auf die Schlagwörter konzentrieren:
-Immobilie schneller, einfacher zum Wunschpreis an Wunschkäufer verkaufen
-Home Staging - Der Schlüssel zu Ihrem Erfolg
- Mit Home Staging die Immobilie erlebbar machen und aus Kaufinteressenten werden Käufer
- Ihre Immobilie wird mit mir zum Bestseller
- professionell ausgebildete Interior Designerin/ Visual Merchandiserin und Home Stagerin bin ich Ihre perfekte Ansprechpartnerin für das erfolgreiche in Szene setzen Ihrer Immobilie
-Der 1. Eindruck zählt, innerhalb von 30 Sekunden entscheidet der Interessent unterbewusst ob Ihm die Immobilie gefällt.
Auf der letzen Seite gerne Kontakt, Foto von mir und das ich Verbandsmitglied der BVRI bin inklusive Logo und Handlungsaufforderung...irgendwie 'gehen sie den nächsten Schritt mit mir' oder 'lassen Sie uns den nächsten Schritt gemeinsam gehen'

```html
<!DOCTYPE html>
<html lang="de">
<head>
<meta charset="utf-8">
<title>Die Raumglanz Idee – Home Staging Flyer</title>
<link rel="stylesheet" href="https://fonts.googleapis.com/css2?family=Nunito:wght@800&family=Questrial&display=swap">
<style>
  :root {
    --page-bg: #dedad6;
    --paper: #ffffff;
    --paper-grey: #ececec;
    --teal-light: #acd8d0;
    --teal: #86bdb3;
    --teal-dark: #6fa89d;
    --teal-text: #5f9f94;
    --ink: #3b3b3b;
    --ink-soft: #555555;
    --line-dark: #4a4a4a;
    --white: #ffffff;
  }
  * { box-sizing: border-box; margin: 0; padding: 0; }
  html, body { width: 1200px; height: 960px; overflow: hidden; }
  body {
    background: var(--page-bg);
    font-family: "Questrial", "Century Gothic", sans-serif;
    color: var(--ink);
    position: relative;
  }
  .spread {
    position: absolute;
    left: 160px;
    width: 880px;
    height: 440px;
    background: var(--paper);
    overflow: hidden;
    box-shadow: 0 6px 18px rgba(0,0,0,.18);
  }
  .spread--outside { top: 20px; }
  .spread--inside { top: 500px; background: var(--paper-grey); }
  .panel { position: absolute; top: 0; height: 440px; width: 293px; overflow: hidden; }
  .panel--about { left: 0; }
  .panel--contact { left: 293px; }
  .panel--cover { left: 587px; width: 293px; }
  .photo { position: absolute; }
  .abs { position: absolute; }

  /* about panel */
  .about__block { left: 17px; top: 16px; width: 264px; height: 400px; background: var(--teal-light); }
  .about__portrait { left: 36px; top: 4px; width: 144px; height: 220px;
    background: linear-gradient(160deg, #e9ece9 0%, #d9d6d0 55%, #c9c2b8 100%); }
  .about__name { left: 139px; top: 40px; width: 99px; height: 20px; background: var(--teal-dark);
    color: var(--white); font-size: 7.5px; letter-spacing: .4px; display: flex; align-items: center; justify-content: center; }
  .about__frame-h { left: 87px; top: 197px; width: 194px; height: 1.5px; background: var(--line-dark); }
  .about__frame-v { left: 87px; top: 197px; width: 1.5px; height: 243px; background: var(--line-dark); }
  .about__corner { left: 238px; top: 20px; width: 30px; height: 32px; border-right: 1.5px solid var(--white); border-bottom: 1.5px solid var(--white); }
  .about__text { left: 110px; top: 255px; width: 160px; font-size: 7.4px; line-height: 1.45; color: var(--ink-soft); }
  .about__headline { font-size: 8.6px; line-height: 1.4; color: var(--ink); margin-bottom: 10px; letter-spacing: .2px; }
  .about__text p + p { margin-top: 8px; }

  /* contact panel */
  .contact__frame { left: 0; top: 25px; width: 262px; height: 376px;
    border: 1.5px solid var(--teal-light); border-right: none; }
  .contact__photo { left: 26px; top: 0; width: 186px; height: 135px;
    background: linear-gradient(180deg, #f1f0ee 0%, #e6e2dc 60%, #c9ab86 100%); }
  .contact__brand { left: 34px; top: 160px; width: 80px; text-align: center; font-size: 8px; letter-spacing: 1.6px; line-height: 1.5; color: var(--teal-text); }
  .contact__cta { left: 124px; top: 230px; width: 120px; font-size: 8px; line-height: 1.4; color: var(--teal-text); }
  .contact__details { left: 124px; top: 285px; width: 160px; font-size: 6.8px; line-height: 1.35; color: var(--ink); }
  .contact__details strong { font-family: "Nunito", sans-serif; font-weight: 800; font-size: 7.6px; }
  .contact__details p + p { margin-top: 9px; }

  /* cover panel */
  .cover__header { left: 0; top: 0; width: 293px; height: 125px; background: var(--teal); }
  .cover__photo { left: 0; top: 125px; width: 293px; height: 315px;
    background: linear-gradient(180deg, #eeeeee 0%, #d8d8d8 55%, #8f8f90 100%); }
  .cover__line-h { left: 0; top: 25px; width: 266px; height: 1.5px; background: var(--white); opacity: .8; }
  .cover__line-v { left: 265px; top: 25px; width: 1.5px; height: 370px; background: var(--white); opacity: .8; }
  .cover__title { left: 30px; top: 50px; color: var(--white); }
  .title-big { font-family: "Nunito", sans-serif; font-weight: 800; font-size: 26px; letter-spacing: .6px; line-height: 1; }
  .cover__subtitle { font-size: 14px; color: var(--ink); margin: 4px 0 0 22px; }
  .cover__brand-box { left: 138px; top: 238px; width: 103px; height: 202px; background: var(--paper-grey);
    display: flex; flex-direction: column; align-items: center; justify-content: center; gap: 10px; }
  .brand-name { font-size: 11px; letter-spacing: 2.4px; line-height: 1.5; text-align: center; color: var(--teal-text); }
  .brand-sub { font-size: 5.6px; letter-spacing: 1.6px; line-height: 1.6; text-align: center; color: var(--teal-text); }

  /* inside spread */
  .inside__bedroom { left: 19px; top: 24px; width: 356px; height: 294px;
    background: linear-gradient(170deg, #b7aeab 0%, #cfc8c4 45%, #e7e3df 70%, #bfa88a 100%); }
  .inside__kids { left: 41px; top: 288px; width: 164px; height: 131px;
    background: linear-gradient(180deg, #f2f2f2 0%, #dedcd8 55%, #c9a84a 100%); }
  .inside__frame { left: 32px; top: 10px; width: 540px; height: 62px; border-left: 1.5px solid var(--teal-light); border-bottom: 1.5px solid var(--teal-light); }
  .inside__title { left: 50px; top: 38px; color: var(--white); }
  .inside__title .title-big { font-size: 27px; opacity: .92; }
  .inside__claim { font-size: 20px; line-height: 1.25; margin-top: 14px; color: var(--white); opacity: .92; }
  .impression { left: 324px; top: 151px; width: 180px; height: 270px; background: var(--teal-dark); color: var(--white);
    padding: 20px 16px 0 19px; font-size: 7.6px; line-height: 1.4; }
  .impression h2 { font-family: "Nunito", sans-serif; font-weight: 800; font-size: 8.6px; letter-spacing: .3px; margin-bottom: 13px; }
  .impression p + p { margin-top: 10px; }
  .inside__after { left: 504px; top: 151px; width: 376px; height: 270px;
    background: linear-gradient(180deg, #f3f3f3 0%, #e2e2e2 50%, #a9a9aa 100%); }
  .inside__before { left: 648px; top: 18px; width: 232px; height: 147px;
    background: linear-gradient(180deg, #d8d8d6 0%, #bdbcba 55%, #8a8987 100%); }
  .inside__before-line { left: 738px; top: 48px; width: 142px; height: 1.5px; background: var(--white); }
  .inside__before-line-v { left: 738px; top: 18px; width: 1.5px; height: 30px; background: var(--white); }
  .label-box { padding: 12px 12px; }
  .label-box h3 { font-size: 17px; font-weight: 400; letter-spacing: .6px; margin-bottom: 6px; }
  .label-box p { font-size: 6.6px; line-height: 1.3; }
  .before-label { left: 574px; top: 28px; width: 128px; height: 103px; background: var(--paper-grey); color: var(--ink); }
  .after-label { left: 755px; top: 185px; width: 125px; height: 100px; background: var(--teal-dark); color: var(--white); }
  .after-label h3 { font-family: "Nunito", sans-serif; font-weight: 800; font-size: 16px; }
  .inside__base-line { left: 0; top: 421px; width: 880px; height: 1.5px; background: #bdbdbd; }
  .inside__rule-v { left: 558px; top: 360px; width: 1.5px; height: 80px; background: var(--line-dark); }
</style>
</head>
<body>

<section class="spread spread--outside" aria-label="Außenseite">
  <div class="panel panel--about">
    <div class="abs about__block"></div>
    <div class="photo about__portrait" role="img" aria-label="Porträtfoto der Home Stagerin in hellem Shirt"></div>
    <div class="abs about__corner"></div>
    <div class="abs about__name">LENA BEISPIEL</div>
    <div class="abs about__frame-h"></div>
    <div class="abs about__frame-v"></div>
    <div class="abs about__text">
      <h2 class="about__headline">IHRE IMMOBILIE WIRD MIT<br>MIR ZUM BESTSELLER</h2>
      <p>Als professionell ausgebildete Interior Designerin / Visual Merchandiserin und Home Stagerin bin ich Ihre perfekte Ansprechpartnerin für das erfolgreiche in Szene setzen Ihrer Immobilie.</p>
      <p>Gemeinsam bringen wir Ihre Immobilie nach vorn.</p>
    </div>
  </div>

  <div class="panel panel--contact">
    <div class="abs contact__frame"></div>
    <div class="photo contact__photo" role="img" aria-label="Heller gestagter Flur mit Spiegel, Pflanze und Holzschriftzug"></div>
    <div class="abs contact__brand">DIE<br>RAUMGLANZ<br>IDEE</div>
    <p class="abs contact__cta">Verkaufen Sie Ihre nächste Immobilie erfolgreich mit mir</p>
    <div class="abs contact__details">
      <p><strong>Die Raumglanz Idee</strong><br>Home Staging &amp; Raumgestaltung</p>
      <p>Lena Beispiel<br>Lindenweg 7<br>54321 Beispielstadt</p>
      <p>0987 654321<br>info@raumglanzidee.de</p>
      <p>www.raumglanzidee.de</p>
    </div>
  </div>

  <div class="panel panel--cover">
    <div class="abs cover__header"></div>
    <div class="photo cover__photo" role="img" aria-label="Gestagter Essbereich mit Rattanleuchte, Rundtisch, schwarzen Stühlen und Wandbild"></div>
    <div class="abs cover__line-h"></div>
    <div class="abs cover__line-v"></div>
    <div class="abs cover__title">
      <h1 class="title-big">HOME STAGING</h1>
      <p class="cover__subtitle">Der Schlüssel zu Ihrem Erfolg</p>
    </div>
    <div class="abs cover__brand-box">
      <p class="brand-name">DIE<br>RAUMGLANZ<br>IDEE</p>
      <p class="brand-sub">HOME STAGING &amp;<br>RAUMGESTALTUNG</p>
    </div>
  </div>
</section>

<section class="spread spread--inside" aria-label="Innenseite">
  <div class="photo inside__bedroom" role="img" aria-label="Gestagtes Schlafzimmer mit Doppelbett, Schaukelstuhl und Spiegel"></div>
  <div class="abs inside__frame"></div>
  <div class="abs inside__title">
    <h2 class="title-big">HOME STAGING</h2>
    <p class="inside__claim">Macht Ihre Immobilie<br>zum Blickfang</p>
  </div>
  <div class="photo inside__kids" role="img" aria-label="Gestagtes Kinderzimmer mit Spielteppich und gelben Akzenten"></div>

  <div class="abs impression">
    <h2>DER 1. EINDRUCK ZÄHLT</h2>
    <p>Innerhalb von 30 Sekunden entscheidet der Interessent unterbewusst ob Ihm eine Immobilie gefällt.</p>
    <p>Mit Home Staging können Sie die Immobilie erlebbar machen und aus Kaufinteressenten werden Käufer.</p>
    <p>Verkaufen Sie die Immobilie schneller, einfacher und zum Ihrem Wunschpreis an Wunschkäufer.</p>
  </div>

  <div class="photo inside__after" role="img" aria-label="Wohnraum nachher, eingerichtet mit Esstisch, Rattanstühlen und Sofa"></div>
  <div class="photo inside__before" role="img" aria-label="Leerer Wohnraum vorher mit Baustellenresten"></div>
  <div class="abs inside__before-line-v"></div>
  <div class="abs inside__before-line"></div>

  <div class="abs label-box before-label">
    <h3>VORHER</h3>
    <p>Ohne Home Staging<br>3 Monate auf dem Markt,<br>15 Besichtigungen und<br>keine Kaufzusage</p>
  </div>
  <div class="abs label-box after-label">
    <h3>NACHHER</h3>
    <p>Mit Home Staging<br>11 Kaufzusagen innerhalb<br>von 2 Tagen, verkauft zum<br>Wunschpreis</p>
  </div>
  <div class="abs inside__rule-v"></div>
  <div class="abs inside__base-line"></div>
</section>

</body>
</html>
```